Website for company called VORENTbio

We need a website for our new company called VORENTbio which developed a platform/technology to identify antigen-specific T cells (immune cells) which can be used for cancer therapy, autoimmunity, etc.

The platform is called VORENT and is rapid, versatile, unbiased, and inexpensive.

We have a semi-final logo although we are not completely set on color and font of text (attached).

Target Market(s)

Our target audience at the moment would be potential investors and VCs. We eventually are interested in getting attention from scientists and cell/immunotherapy companies.

Industry/Entity Type

Healthcare/Technology

Coding

Coded - Design and coding required

Number of Pages Required

1 page

Colors
0094D4
00A9DD
6FCCEA
C7EBF8
E9F6FB
00AB8E
00BBA5
67D7C9
C6EFE9
E9F9F6
E54698
E96AAD
F1A4CE
F9D9EA
FCEFF6
A7469A
B969AE
D3A5CF
EDDBEB
F8F0F9
6B429C
8869AF
B7A5CE
E3DAEB
F3F0F8

Requirements
Must have
• Landing page about the company, About us page, Technology page (could be merged with company landing page), Contact us page

```html
<!DOCTYPE html>
<html lang="en">
<head>
<meta charset="utf-8">
<title>VORENTbio</title>
<link rel="stylesheet" href="https://fonts.googleapis.com/css2?family=Poppins:ital,wght@0,400;0,500;0,600;0,700;1,400&family=Comfortaa:wght@400;500&display=swap">
<style>
:root{
  --blue:#0094d4;
  --blue-mid:#00a9dd;
  --blue-light:#6fccea;
  --blue-pale:#c7ebf8;
  --blue-deep:#0a6fb8;
  --ink:#111;
  --text:#444;
  --muted:#777;
  --grey-bg:#efefef;
  --footer-bg:#f1f1f1;
  --white:#fff;
  --star:#f5b800;
}
*{margin:0;padding:0;box-sizing:border-box}
html,body{width:1200px;height:5168px;overflow:hidden}
body{position:relative;font-family:"Poppins",sans-serif;color:var(--text);background:var(--white)}
.abs{position:absolute}
.brand{font-family:"Poppins",sans-serif;font-weight:600;letter-spacing:-0.5px}
.heading{font-family:"Comfortaa",sans-serif;font-weight:500;color:var(--blue);letter-spacing:2px;white-space:nowrap}
.kicker{font-family:"Poppins",sans-serif;font-weight:600;font-size:14px;color:var(--ink);display:flex;align-items:center;gap:8px}
.kicker::before,.kicker::after{content:"";display:block;width:52px;height:2px;background:var(--ink)}
.dot-mark{border-radius:50%;background:var(--ink)}
.btn{position:absolute;display:flex;align-items:center;justify-content:center;background:var(--blue);color:var(--white);font-weight:600;font-size:14px;border-radius:6px}
.pager{position:absolute;display:flex;gap:5px}
.pager span{width:9px;height:9px;border:1.5px solid #555;border-radius:50%}
.pager span.on{background:#333}

/* header */
.topbar{left:0;top:0;width:1200px;height:108px;background:var(--blue)}
.nav{left:420px;top:45px;display:flex;gap:18px;font-size:13px;color:var(--white)}
.nav .active{font-weight:600}
.callbox{left:860px;top:0;width:340px;height:124px;background:var(--blue-mid);clip-path:polygon(0 0,100% 0,100% 100%,8% 100%)}
.callbox .label{position:absolute;left:84px;top:28px;font-size:13px;font-weight:600;color:var(--white)}
.callbox .num{position:absolute;left:34px;top:62px;font-size:28px;color:var(--white)}
.callbox .ring{position:absolute;left:38px;top:20px;width:34px;height:34px;border:2px solid var(--white);border-radius:50%}

/* hero */
.hero-photo{left:0;top:108px;width:820px;height:600px;background:linear-gradient(90deg,#0b3f79 0%,#1f78c8 40%,#6db5e6 70%,rgba(255,255,255,0) 100%)}
.hero .welcome{left:668px;top:288px;font-size:17px;font-weight:600;color:var(--blue)}
.hero .brand{left:664px;top:308px;font-size:78px;color:var(--ink);font-weight:700;letter-spacing:-1px}
.hero .lead{left:668px;top:402px;width:450px;font-size:13px;line-height:24px;color:#333}

/* services */
.services-bg{left:0;top:708px;width:1200px;height:870px;background:var(--grey-bg)}
.card{position:absolute;background:var(--white);box-shadow:0 2px 10px rgba(0,0,0,.12);border-radius:4px}
.card .ph{position:absolute;border-radius:2px}
.card h3{position:absolute;width:100%;text-align:center;font-family:"Comfortaa",sans-serif;font-weight:500;font-size:27px;color:var(--blue);letter-spacing:2px}
.card p{position:absolute;left:22px;right:22px;text-align:center;font-size:12.5px;line-height:26px;color:#555}

/* about */
.about h2{left:210px;top:1718px;font-size:44px}
.about .lede{left:122px;top:1820px;width:456px;font-size:20px;font-weight:600;line-height:32px;color:var(--ink);text-align:justify}
.about .body{left:122px;top:1896px;width:456px;font-size:13.5px;line-height:27px;color:#333;text-align:justify}
.about-art{left:626px;top:1650px;width:500px;height:550px;background:radial-gradient(circle at 50% 55%,#f6a83c 0%,#2d6fd6 22%,#1a3fb0 45%,#c8dcf6 75%,#fff 100%)}

/* features */
.band{left:0;top:2288px;width:1200px;height:284px;background:linear-gradient(180deg,#1a89d2,#0f6fbd)}
.feature{position:absolute;width:220px;text-align:center}
.feature .disc{width:132px;height:132px;margin:0 auto;border-radius:50%;background:var(--white);display:flex;align-items:center;justify-content:center;box-shadow:0 0 0 4px rgba(255,255,255,.35)}
.feature .disc svg{width:96px;height:96px}
.feature span{display:block;margin-top:18px;font-family:"Comfortaa",sans-serif;font-size:22px;color:var(--white);letter-spacing:3px}

/* testimonials */
.bubble{position:absolute;width:464px;height:228px;border:2px solid #ddd;border-radius:16px;background:var(--white)}
.bubble .stars{position:absolute;right:24px;top:40px;color:var(--star);font-size:15px;letter-spacing:1px}
.bubble p{position:absolute;left:36px;right:30px;top:80px;font-size:11.5px;line-height:22px;font-style:italic;color:#333}
.quote{position:absolute;font-family:Georgia,serif;font-size:130px;line-height:1;color:var(--blue);font-weight:700}
.avatar{position:absolute;width:66px;height:66px;border-radius:50%;background:linear-gradient(135deg,#c9ced3,#7c858d)}
.who{position:absolute;font-size:13px;line-height:20px}
.who b{font-weight:500;color:var(--blue)}
.who small{display:block;font-size:11px;color:#333}

/* appointment */
.appt-bg{left:0;top:3314px;width:1200px;height:470px;background:radial-gradient(ellipse at 30% 60%,#1b8fd8 0%,#0a6fb8 60%,#075fa3 100%)}
.appt-title{left:136px;top:3462px;font-size:34px;color:var(--white)}
.appt-sub{left:138px;top:3512px;font-size:12px;font-weight:600;color:var(--white);display:flex;align-items:center;gap:8px}
.appt-sub::before,.appt-sub::after{content:"";width:40px;height:2px;background:var(--white)}
.appt-blurb{left:66px;top:3554px;width:480px;font-size:16px;line-height:30px;color:var(--white)}
.field{position:absolute;width:256px;height:74px;background:var(--white);border-radius:6px;display:flex;align-items:center;padding-left:22px;gap:10px;font-size:17px;color:#777}
.field svg{width:22px;height:22px}
.book{left:598px;top:3630px;width:206px;height:54px;background:var(--white);color:var(--blue-deep);font-size:14px;font-weight:500;border-radius:4px}
.appt-or{left:846px;top:3640px;font-size:22px;font-weight:600;color:var(--white)}
.phone-ring{left:886px;top:3630px;width:52px;height:52px;border:2px solid var(--white);border-radius:8px;display:flex;align-items:center;justify-content:center}
.appt-phone{left:948px;top:3640px;font-size:22px;color:var(--white);white-space:nowrap}

/* case studies */
.post{position:absolute;width:316px;height:490px;background:var(--white);box-shadow:0 2px 10px rgba(0,0,0,.13)}
.post .ph{position:absolute;left:14px;top:16px;width:288px;height:210px}
.post .date{position:absolute;left:28px;top:256px;font-size:14px;color:#444;display:flex;align-items:center;gap:8px}
.post .date i{width:14px;height:14px;border:2px solid var(--blue);border-radius:2px;display:block}
.post h4{position:absolute;left:28px;right:20px;top:280px;font-size:18.5px;font-weight:500;line-height:28px;color:var(--ink)}
.post p{position:absolute;left:28px;right:20px;top:342px;font-size:13.5px;line-height:26px;color:#777}
.post .btn{left:28px;top:404px;width:118px;height:44px;font-size:13px;font-weight:500}

/* footer */
.footer{left:0;top:4690px;width:1200px;height:478px;background:var(--footer-bg)}
.social{position:absolute;width:38px;height:38px;border-radius:50%;background:var(--blue)}
.footer-title{position:absolute;top:4804px;font-size:22px;font-weight:500;color:var(--ink)}
.links{left:536px;top:4872px;list-style:none;font-size:13.5px;color:#222}
.links li{height:33px;display:flex;align-items:center;gap:14px}
.links li::before{content:"";width:8px;height:8px;border-radius:50%;background:var(--blue)}
.contact-row{position:absolute;left:796px;display:flex;gap:16px;font-size:13px;line-height:24px;color:#222}
.contact-row .ic{flex:none;width:34px;height:34px;border-radius:50%;background:var(--blue);display:flex;align-items:center;justify-content:center}
.contact-row .ic svg{width:18px;height:18px}
.rule{left:70px;top:5090px;width:1060px;height:1px;background:#d5d5d5}
.copy{left:0;top:5114px;width:1200px;text-align:center;font-size:14px;color:#222}
</style>
</head>
<body>

<!-- header -->
<div class="abs topbar"></div>
<div class="abs brand" style="left:74px;top:28px;font-size:36px;color:#fff;display:flex;align-items:center;gap:10px">
  <span class="dot-mark" style="width:34px;height:34px;background:#fff"></span>vorentbio
</div>
<nav class="abs nav"><span class="active">HOME</span><span>ABOUT US</span><span>SERVICES</span><span>REVIEWS</span><span>CONTACT US</span></nav>
<div class="abs callbox">
  <span class="ring"></span>
  <svg class="abs" style="left:46px;top:28px" width="18" height="18" viewBox="0 0 24 24" fill="none" stroke="#fff" stroke-width="2"><path d="M5 3h4l2 5-2.5 1.5a11 11 0 0 0 6 6L16 13l5 2v4a2 2 0 0 1-2 2A16 16 0 0 1 3 5a2 2 0 0 1 2-2z"/></svg>
  <span class="label">CONTACT US TODAY !</span>
  <span class="num">+91 900 123 4567</span>
</div>

<!-- hero -->
<section class="hero">
  <div class="abs hero-photo" role="img" aria-label="Hand holding a glowing blue virus particle among network nodes"></div>
  <div class="abs welcome">Welcome To</div>
  <div class="abs brand">vorentbio</div>
  <p class="abs lead">Lorem ipsum dolor sit amet, consectetur adipiscing elit, sed do eiusmod tempor incididunt ut labore et dolore magna aliqua.</p>
  <div class="btn" style="left:668px;top:470px;width:244px;height:60px;font-size:13px;font-weight:500">Request an Appointment</div>
</section>

<!-- services -->
<section class="services">
  <div class="abs services-bg"></div>
  <span class="abs dot-mark" style="left:358px;top:820px;width:46px;height:46px"></span>
  <h2 class="abs heading" style="left:438px;top:826px;font-size:40px">Our Services</h2>
  <div class="abs kicker" style="left:494px;top:876px">WHAT WE DO</div>

  <div class="card" style="left:114px;top:962px;width:308px;height:446px">
    <div class="ph" style="left:18px;top:22px;width:272px;height:222px;background:radial-gradient(circle at 60% 60%,#3f9de6,#0b3f8f)" role="img" aria-label="Blue cells under a microscope"></div>
    <h3 style="top:272px">Services 1</h3>
    <p style="top:320px">Lorem ipsum dolor sit amet, consec tetur adipiscing elit, sed do eiusmod tempor incididunt ut labore et dolore</p>
  </div>
  <div class="btn" style="left:196px;top:1384px;width:144px;height:52px">Read more</div>

  <div class="card" style="left:444px;top:962px;width:308px;height:446px">
    <div class="ph" style="left:18px;top:22px;width:272px;height:222px;background:linear-gradient(135deg,#eef1f3,#c9c2b8)" role="img" aria-label="Doctor consulting with a patient"></div>
    <h3 style="top:272px">Services 2</h3>
    <p style="top:320px">Lorem ipsum dolor sit amet, consec tetur adipiscing elit, sed do eiusmod tempor incididunt ut labore et dolore</p>
  </div>
  <div class="btn" style="left:526px;top:1384px;width:144px;height:52px">Read more</div>

  <div class="card" style="left:774px;top:962px;width:308px;height:446px">
    <div class="ph" style="left:18px;top:22px;width:272px;height:222px;background:linear-gradient(135deg,#4f8ee6,#7a4fd6)" role="img" aria-label="Runner figure with DNA strands and cells"></div>
    <h3 style="top:272px">Services 3</h3>
    <p style="top:320px">Lorem ipsum dolor sit amet, consec tetur adipiscing elit, sed do eiusmod tempor incididunt ut labore et dolore</p>
  </div>
  <div class="btn" style="left:856px;top:1384px;width:144px;height:52px">Read more</div>

  <div class="pager" style="left:576px;top:1486px"><span class="on"></span><span></span><span></span><span></span></div>
</section>

<!-- about -->
<section class="about">
  <span class="abs dot-mark" style="left:126px;top:1702px;width:46px;height:46px"></span>
  <h2 class="abs heading">About us</h2>
  <div class="abs kicker" style="left:210px;top:1768px">WHO WE ARE</div>
  <p class="abs lede">Lorem ipsum dolor sit amet, consectetur adipiscing elit,</p>
  <p class="abs body">sed do eiusmod tempor incididunt ut labore et dolore magna aliqua. Ut enim ad minim veniam, quis nostrud exercitation ullamco laboris nisi ut aliquip ex ea commodo consequat. Duis aute irure dolor in reprehenderit in voluptate velit esse cillum dolore eu fugiat nulla pariatur. Excepteur sint occaecat cupidatat non proident, sunt in culpa qui officia deserunt mollit anim id est laborum.</p>
  <div class="btn" style="left:122px;top:2088px;width:166px;height:58px;font-size:13px;font-weight:500">View More</div>
  <div class="abs about-art" role="img" aria-label="Glowing blue molecular structure illustration"></div>
</section>

<!-- features -->
<section>
  <div class="abs band" role="img" aria-label="Blue band with faint virus particles"></div>
  <div class="feature" style="left:72px;top:2340px">
    <div class="disc"><svg viewBox="0 0 96 96" fill="none" stroke="#0a6fb8" stroke-width="2.5"><circle cx="48" cy="48" r="30" stroke-dasharray="6 4"/><circle cx="48" cy="48" r="16"/><path d="M48 40v16M43 44h8a3 3 0 0 1 0 6h-6a3 3 0 0 0 0 6h8"/></svg></div>
    <span>Rapid</span>
  </div>
  <div class="feature" style="left:340px;top:2340px">
    <div class="disc"><svg viewBox="0 0 96 96" fill="none" stroke="#0a6fb8" stroke-width="2.5"><path d="M48 78V30M48 30l-10 10M48 30l10 10M30 66V48l-10-10M66 66V48l10-10M20 38v10M20 38h10M76 38v10M76 38H66"/></svg></div>
    <span>versatile</span>
  </div>
  <div class="feature" style="left:610px;top:2340px">
    <div class="disc"><svg viewBox="0 0 96 96" fill="none" stroke="#0a6fb8" stroke-width="2.5"><path d="M48 22c-10 0-16 6-16 14-6 2-6 12 0 14 0 8 8 12 16 10 8 2 16-2 16-10 6-2 6-12 0-14 0-8-6-14-16-14zM48 22v38"/><path d="M20 56v14l16 8M76 56v14l-16 8"/></svg></div>
    <span>unbiased</span>
  </div>
  <div class="feature" style="left:892px;top:2340px">
    <div class="disc"><svg viewBox="0 0 96 96" fill="none" stroke="#0a6fb8" stroke-width="2.5"><path d="M26 40a24 24 0 0 1 44-8M70 56a24 24 0 0 1-44 8M70 22v10H60M26 74V64h10"/><path d="M48 36v24M42 41h9a4 4 0 0 1 0 7h-6a4 4 0 0 0 0 7h10"/></svg></div>
    <span>inexpensive</span>
  </div>
</section>

<!-- testimonials -->
<section>
  <span class="abs dot-mark" style="left:358px;top:2672px;width:46px;height:46px"></span>
  <h2 class="abs heading" style="left:438px;top:2680px;font-size:40px">Our testimonials</h2>
  <div class="abs kicker" style="left:518px;top:2730px">CLIENT REVIEWS</div>

  <div class="bubble" style="left:100px;top:2862px">
    <div class="stars">★★★★★</div>
    <p>Lorem ipsum dolor sit amet, consectetur adipiscing elit, sed do eiusmod tempor incididunt ut labore et dolore magna aliqua. Ut enim ad minim veniam, quis nostrud exercitation ullamco laboris nisi ut aliquip ex ea commodo consequat.</p>
  </div>
  <div class="quote" style="left:164px;top:2820px">“</div>
  <div class="avatar" style="left:210px;top:3114px" role="img" aria-label="Client portrait"></div>
  <div class="who" style="left:292px;top:3130px"><b>MARCUS HALE</b><small>Lorem ipsum</small></div>

  <div class="bubble" style="left:610px;top:2862px">
    <div class="stars">★★★★★</div>
    <p>Lorem ipsum dolor sit amet, consectetur adipiscing elit, sed do eiusmod tempor incididunt ut labore et dolore magna aliqua. Ut enim ad minim veniam, quis nostrud exercitation ullamco laboris nisi ut aliquip ex ea commodo consequat. Duis aute irure dolor in reprehenderit in voluptate velit.</p>
  </div>
  <div class="quote" style="left:674px;top:2820px">“</div>
  <div class="avatar" style="left:718px;top:3114px" role="img" aria-label="Client portrait"></div>
  <div class="who" style="left:800px;top:3130px"><b>DANIEL REYES</b><small>Lorem ipsum</small></div>

  <div class="pager" style="left:552px;top:3228px"><span class="on"></span><span></span><span></span><span></span></div>
</section>

<!-- appointment -->
<section>
  <div class="abs appt-bg" role="img" aria-label="Blue background with soft molecular shapes"></div>
  <span class="abs dot-mark" style="left:70px;top:3456px;width:50px;height:50px;background:#fff"></span>
  <h2 class="abs heading appt-title">Get an Appointment</h2>
  <div class="abs appt-sub">VORENT</div>
  <p class="abs appt-blurb">Our team of highly trained professionals uses the latest healing technologies to restore you to pain-free health quickly and easily.</p>

  <div class="field" style="left:598px;top:3430px"><svg viewBox="0 0 24 24" fill="none" stroke="#0094d4" stroke-width="2"><circle cx="12" cy="8" r="4"/><path d="M4 21a8 8 0 0 1 16 0"/></svg>Name</div>
  <div class="field" style="left:870px;top:3430px"><svg viewBox="0 0 24 24" fill="none" stroke="#0094d4" stroke-width="2"><rect x="3" y="5" width="18" height="14" rx="2"/><path d="M3 7l9 6 9-6"/></svg>Email</div>
  <div class="field" style="left:598px;top:3526px"><svg viewBox="0 0 24 24" fill="none" stroke="#0094d4" stroke-width="2"><path d="M5 3h4l2 5-2.5 1.5a11 11 0 0 0 6 6L16 13l5 2v4a2 2 0 0 1-2 2A16 16 0 0 1 3 5a2 2 0 0 1 2-2z"/></svg>Phone</div>
  <div class="field" style="left:870px;top:3526px"><svg viewBox="0 0 24 24" fill="none" stroke="#0094d4" stroke-width="2"><path d="M6 3h12v18l-6-4-6 4z"/></svg>Subjuct</div>

  <div class="btn book">BOOK APPOINTMENT</div>
  <div class="abs appt-or">or</div>
  <div class="abs phone-ring">
    <svg width="24" height="24" viewBox="0 0 24 24" fill="none" stroke="#fff" stroke-width="2"><path d="M5 3h4l2 5-2.5 1.5a11 11 0 0 0 6 6L16 13l5 2v4a2 2 0 0 1-2 2A16 16 0 0 1 3 5a2 2 0 0 1 2-2z"/></svg>
  </div>
  <div class="abs appt-phone">+91 900 123 4567</div>
</section>

<!-- case studies -->
<section>
  <span class="abs dot-mark" style="left:400px;top:3886px;width:46px;height:46px"></span>
  <h2 class="abs heading" style="left:480px;top:3894px;font-size:40px">case studys</h2>
  <div class="abs kicker" style="left:538px;top:3944px">OUR BLOGS</div>

  <article class="post" style="left:104px;top:4030px">
    <div class="ph" style="background:radial-gradient(circle at 30% 55%,#4a8fd6,#101420 45%,#e05a24 70%,#1a0f10)" role="img" aria-label="Blue and orange cells colliding"></div>
    <div class="date"><i></i>June 22, 2025</div>
    <h4>Lorem ipsum dolor sit amet, consectetur elit dol</h4>
    <p>Lorem ipsum dolor sit amet, con sectetur adipiscing elit, sed do ei</p>
    <div class="btn">Read More</div>
  </article>
  <article class="post" style="left:440px;top:4030px">
    <div class="ph" style="background:radial-gradient(circle at 55% 60%,#3a5a46,#0f3a2a 55%,#06140e)" role="img" aria-label="Green virus particle close-up"></div>
    <div class="date"><i></i>June 22, 2025</div>
    <h4>Lorem ipsum dolor sit amet, consectetur elit dol</h4>
    <p>Lorem ipsum dolor sit amet, con sectetur adipiscing elit, sed do ei</p>
    <div class="btn">Read More</div>
  </article>
  <article class="post" style="left:776px;top:4030px">
    <div class="ph" style="background:radial-gradient(circle at 55% 50%,#e0503a,#3f8ad8 25%,#0f4f9a)" role="img" aria-label="Blue cells with a red cell in focus"></div>
    <div class="date"><i></i>June 22, 2025</div>
    <h4>Lorem ipsum dolor sit amet, consectetur elit dol</h4>
    <p>Lorem ipsum dolor sit amet, con sectetur adipiscing elit, sed do ei</p>
    <div class="btn">Read More</div>
  </article>

  <div class="pager" style="left:574px;top:4616px"><span class="on"></span><span></span><span></span><span></span></div>
</section>

<!-- footer -->
<footer>
  <div class="abs footer"></div>
  <div class="abs brand" style="left:110px;top:4862px;font-size:42px;color:#111;display:flex;align-items:center;gap:12px">
    <span class="dot-mark" style="width:48px;height:48px"></span>vorentbio
  </div>
  <span class="social" style="left:202px;top:4950px"></span>
  <span class="social" style="left:250px;top:4950px"></span>
  <span class="social" style="left:298px;top:4950px"></span>

  <h5 class="footer-title" style="left:536px">LINKS</h5>
  <ul class="abs links">
    <li>About Us</li><li>Services</li><li>Testimonials</li><li>Contact Us</li>
  </ul>

  <h5 class="footer-title" style="left:794px">CONTACT US</h5>
  <div class="contact-row" style="top:4872px">
    <span class="ic"><svg viewBox="0 0 24 24" fill="#fff"><path d="M12 2a7 7 0 0 0-7 7c0 5 7 13 7 13s7-8 7-13a7 7 0 0 0-7-7zm0 9.5A2.5 2.5 0 1 1 12 6.5a2.5 2.5 0 0 1 0 5z"/></svg></span>
    <span style="width:240px">234, Lorem ipsum,Lorem ipsum, Lorem ipsum.</span>
  </div>
  <div class="contact-row" style="top:4946px">
    <span class="ic"><svg viewBox="0 0 24 24" fill="none" stroke="#fff" stroke-width="2"><path d="M5 3h4l2 5-2.5 1.5a11 11 0 0 0 6 6L16 13l5 2v4a2 2 0 0 1-2 2A16 16 0 0 1 3 5a2 2 0 0 1 2-2z"/></svg></span>
    <span style="line-height:34px">+91 900 123 4567</span>
  </div>
  <div class="contact-row" style="top:4998px">
    <span class="ic"><svg viewBox="0 0 24 24" fill="none" stroke="#fff" stroke-width="2"><rect x="3" y="5" width="18" height="14" rx="2"/><path d="M3 7l9 6 9-6"/></svg></span>
    <span style="line-height:34px">info@vorentbio-mail.com</span>
  </div>

  <div class="abs rule"></div>
  <div class="abs copy">Copyright © 2025 All Rights Reserved By Company Name</div>
</footer>

</body>
</html>
```